Your After-Split Lantern: Sensible, Everyday Guidance for the Freshly Solo

I need a wraparound book cover design for a ~132-page workbook. Trim size will be 8.5x11 and the book will be on 60# paper. The name of this project is the name and subtitle of the book. Here's the synopsis I've come up with, which should be included on the back cover (without the quote marks):
"So you're divorced. What do you do now? There are probably a whole bunch of
things you never thought of, like:
- Cleaning up and automating your finances
- Making sure your insurance coverages are all correct
- Removing your former spouse's name from your assets and liabilities
- Building your personal team of financial advisors
Are you aware you need to take care of these things, but you don't know where to
start? This workbook is perfect for you. You'll be led, step by step, through detailed
explanations of how to do everything on this list, and much, much more!"
Here's the author bio for the back cover:
"Gregory T. Halvorsen, Esq. graduated from Brantwell College School of Law in 2002 and has been a practicing trial lawyer in the Metro Atlanta area ever since. Family law has always been a big part of Greg's practice. Throughout his career, Greg has helped hundreds of people through their divorce cases, and now through this book, Greg looks forward to being able to help them after the dust settles."
I have an ISBN bar code ready to go, so leave space for it on the back cover in the bottom right corner (winner will be expected to add the bar code graphic to the finished product).
This will be a print-on-demand book through Quillora's PressNest. They have a sizing template if you want to grab it for yourself.
Target Market(s)
Primarily divorced women, especially middle-aged and older

```html
<!DOCTYPE html>
<html lang="en">
<head>
<meta charset="utf-8">
<title>Your After-Split Lantern — Wraparound Cover</title>
<link rel="stylesheet" href="https://fonts.googleapis.com/css2?family=Bebas+Neue&family=Open+Sans:wght@400;600&display=swap">
<style>
  :root {
    --paper: #e7e8e4;
    --orange: #f15a22;
    --teal: #2b95a5;
    --ink: #4c575d;
    --soft-ink: #6a7377;
    --tick: #c0392b;
  }
  * { margin: 0; padding: 0; box-sizing: border-box; }
  html, body { width: 1200px; height: 763px; overflow: hidden; background: var(--paper); }
  .cover { position: relative; width: 1200px; height: 763px; background: var(--paper); font-family: "Open Sans", Arial, sans-serif; color: var(--ink); }

  .title-block { position: absolute; text-align: center; font-family: "Bebas Neue", Impact, sans-serif; }
  .title-top { color: var(--orange); line-height: 1; }
  .title-main { color: var(--teal); line-height: 0.9; text-shadow: 1px 2px 2px rgba(0,0,0,0.18); }
  .subtitle { color: var(--ink); line-height: 1.05; }

  .back-title { left: 60px; width: 472px; top: 22px; }
  .back-title .title-top { font-size: 44px; }
  .back-title .title-main { font-size: 86px; }
  .back-title .subtitle { font-size: 20px; margin-top: 8px; }

  .front-title { left: 660px; width: 490px; top: 26px; }
  .front-title .title-top { font-size: 58px; }
  .front-title .title-main { font-size: 140px; }
  .front-title .subtitle { font-size: 29px; margin-top: 14px; }

  .synopsis { position: absolute; left: 84px; top: 194px; width: 480px; font-size: 14.6px; font-weight: 600; line-height: 1.33; }
  .synopsis p + ul, .synopsis ul + p { margin-top: 14px; }
  .checklist { list-style: none; margin-left: 2px; }
  .checklist li { display: flex; align-items: center; gap: 7px; }
  .checklist svg { flex: none; }

  .author-bio { position: absolute; left: 60px; top: 462px; width: 508px; padding: 18px 24px 22px; font-size: 11.4px; line-height: 1.45; color: var(--soft-ink); background: var(--paper); box-shadow: 0 6px 26px rgba(0,0,0,0.18); border-radius: 4px; }

  .front-art { position: absolute; left: 745px; top: 300px; width: 320px; height: 370px; border-radius: 46% 46% 40% 40%; background: radial-gradient(ellipse at 45% 55%, #f4efe2 0%, #cfc7b6 45%, #a8a598 70%, rgba(231,232,228,0) 72%); }

  .author-name { position: absolute; left: 660px; width: 490px; top: 708px; text-align: center; font-family: "Bebas Neue", Impact, sans-serif; font-size: 38px; letter-spacing: 3px; color: var(--ink); }
</style>
</head>
<body>
<main class="cover">
  <section class="back-cover">
    <header class="title-block back-title">
      <div class="title-top">Your After-Split</div>
      <div class="title-main">Lantern</div>
      <div class="subtitle">Sensible, Everyday Guidance for the Freshly Solo</div>
    </header>

    <div class="synopsis">
      <p>So you're divorced. What do you do now? There are probably a whole bunch of things you never thought of, like:</p>
      <ul class="checklist">
        <li><svg width="12" height="12" viewBox="0 0 12 12"><circle cx="6" cy="6" r="5.5" fill="#fff" stroke="#b9b9b9"/><path d="M3 6.2l2 2 4-4.6" fill="none" stroke="var(--tick)" stroke-width="1.8"/></svg>Cleaning up and automating your finances</li>
        <li><svg width="12" height="12" viewBox="0 0 12 12"><circle cx="6" cy="6" r="5.5" fill="#fff" stroke="#b9b9b9"/><path d="M3 6.2l2 2 4-4.6" fill="none" stroke="var(--tick)" stroke-width="1.8"/></svg>Making sure your insurance coverages are all correct</li>
        <li><svg width="12" height="12" viewBox="0 0 12 12"><circle cx="6" cy="6" r="5.5" fill="#fff" stroke="#b9b9b9"/><path d="M3 6.2l2 2 4-4.6" fill="none" stroke="var(--tick)" stroke-width="1.8"/></svg>Removing your former spouse's name from your assets and liabilities</li>
        <li><svg width="12" height="12" viewBox="0 0 12 12"><circle cx="6" cy="6" r="5.5" fill="#fff" stroke="#b9b9b9"/><path d="M3 6.2l2 2 4-4.6" fill="none" stroke="var(--tick)" stroke-width="1.8"/></svg>Building your personal team of financial advisors</li>
      </ul>
      <p>Are you aware you need to take care of these things, but you don't know where to start? This workbook is perfect for you. You'll be led, step by step, through detailed explanations of how to do everything on this list, and much, much more!</p>
    </div>

    <p class="author-bio">Gregory T. Halvorsen, Esq. graduated from Brantwell College School of Law in 2002 and has been a practicing trial lawyer in the Metro Atlanta area ever since. Family law has always been a big part of Greg's practice. Throughout his career, Greg has helped hundreds of people through their divorce cases, and now through this book, Greg looks forward to being able to help them after the dust settles.</p>
  </section>

  <section class="front-cover">
    <header class="title-block front-title">
      <div class="title-top">Your After-Split</div>
      <div class="title-main">Lantern</div>
      <div class="subtitle">Sensible, Everyday Guidance for<br>the Freshly Solo</div>
    </header>

    <div class="front-art" role="img" aria-label="Open brass and silver pocket compass with its lid raised"></div>

    <div class="author-name">Gregory T. Halvorsen, Esq.</div>
  </section>
</main>
</body>
</html>
```